Website for International Non-Profit for Birth Parent Searching

Tovira is a 501(c)(3) non-profit organization that helps Chinese adoptees search and reunite with birth families who were separated due the One Child Policy in China. We want to create a website that can link to an information database that allows website users to easily access information around search ads in an organized way; help connect families to professional searchers; provide resources for community support for adoptees and their families as they embark on a personal and emotional journey of finding birth family through support groups on social media and consultation/education on the searching process; and provide the opportunity for the adoptive community to give back through donations and volunteer opportunities. The final design should foster a sense of community and be easy navigable to access the multiple resources we provide to help families search for each other. We would like to see designs with red/black/white color schemes that are gentle, inviting, and family friendly to viewers. We would like to see some design layouts with Chinese themes, if possible.

```html
<!DOCTYPE html>
<html lang="en">
<head>
<meta charset="utf-8">
<title>Tovira – International Non-Profit for Birth Parent Searching</title>
<link rel="stylesheet" href="https://fonts.googleapis.com/css2?family=Montserrat:wght@400;500;600;700&family=Lato:wght@400;700&display=swap">
<style>
:root{
  --red:#9a0b13;
  --red-bright:#e8463c;
  --ink:#1b1b1b;
  --text:#2a2a2a;
  --white:#ffffff;
  --card:#d9d9d9;
  --arrow:#8a8a8a;
  --line:#a8a8a8;
  --footer:#111111;
  --footer-text:#bdbdbd;
}
*{margin:0;padding:0;box-sizing:border-box}
html,body{width:1200px;height:3990px;overflow:hidden;background:var(--white)}
body{position:relative;font-family:"Montserrat",sans-serif;color:var(--text)}
.line{display:block;white-space:nowrap}
.btn{position:absolute;display:flex;align-items:center;justify-content:center;background:var(--red);color:var(--white);font-family:"Montserrat",sans-serif;font-weight:500;font-size:17px;letter-spacing:.3px;text-transform:uppercase}

/* Hero */
.hero{position:absolute;left:0;top:0;width:1200px;height:700px}
.hero-backdrop{position:absolute;left:0;top:0}
.brand{position:absolute;left:144px;top:16px;font-size:46px;font-weight:600;color:var(--white);letter-spacing:.5px;line-height:56px}
.nav{position:absolute;top:30px;left:0;font-size:17px;color:var(--white)}
.nav span{position:absolute;white-space:nowrap}
.nav .active{color:var(--red-bright)}
.search-ads{position:absolute;left:935px;top:20px;width:121px;height:42px;border:1.5px solid var(--white);color:var(--white);font-size:17px;display:flex;align-items:center;justify-content:center}
.hero-title{position:absolute;right:145px;top:228px;text-align:right;color:var(--white);font-weight:700;font-size:40px;line-height:45px}
.slide-arrow{position:absolute;top:317px;width:42px;height:42px}

/* Welcome */
.section-title{position:absolute;left:0;width:1200px;text-align:center;font-weight:500;font-size:33px;color:var(--ink)}
.welcome-text{position:absolute;left:0;top:822px;width:1200px;text-align:center;font-family:"Lato",sans-serif;font-size:17px;line-height:32px;color:var(--text)}

/* Steps */
.steps-bg{position:absolute;left:0;top:1058px;width:1200px;height:520px;background:linear-gradient(100deg,#f6d3e0 0%,#f6eef2 25%,#f3f6f4 50%,#d8efee 75%,#bfe4e6 92%,#f3d2df 100%)}
.step-line{position:absolute;top:1286px;height:3px;background:var(--line)}
.step-circle{position:absolute;top:1208px;width:158px;height:158px;border-radius:50%;background:var(--white);border:2px solid #9a9a9a;display:flex;align-items:center;justify-content:center}
.step{position:absolute;top:1388px;width:290px;text-align:center}
.step-num{font-size:16px;font-weight:600;color:var(--ink)}
.step-name{font-size:25px;font-weight:600;color:var(--red);margin-top:3px}
.step-desc{font-family:"Lato",sans-serif;font-size:11px;line-height:20px;color:var(--ink);margin-top:3px}

/* Cards */
.card{position:absolute;width:288px;height:383px;background:var(--card)}
.card-photo{width:288px;height:191px}
.card-title{margin:17px 13px 0;font-size:16.5px;font-weight:400;line-height:27px;color:var(--ink)}
.card-text{margin:8px 13px 0;font-family:"Lato",sans-serif;font-size:11px;line-height:20px;color:var(--ink)}
.card-arrow{position:absolute;left:12px;top:338px}

/* Banner */
.banner{position:absolute;left:0;top:2278px;width:1200px;height:464px;background:radial-gradient(ellipse at 55% 50%,#fbfbf4 0%,#eef2dc 45%,#c8d99c 80%,#a9c57d 100%)}
.banner-photo{position:absolute;left:143px;top:2322px;width:374px;height:374px;border-radius:50%;background:radial-gradient(circle at 55% 45%,#f3d9b8 0%,#c79a6a 45%,#3a2a22 100%)}
.banner-quote{position:absolute;right:147px;top:2378px;text-align:right;font-size:24px;font-weight:500;line-height:40px;color:var(--ink)}

/* Contact */
.contact{position:absolute;left:0;top:3425px;width:1200px;height:454px;background:linear-gradient(135deg,#a50f18 0%,#8f0a12 50%,#a3101a 100%)}
.field{position:absolute;border:1px solid rgba(255,255,255,.85);color:var(--white);font-family:"Lato",sans-serif;font-size:12px;padding:0 15px;display:flex;align-items:center}
.field.area{align-items:flex-start;padding-top:12px}
.submit{background:var(--ink)}

/* Footer */
.footer{position:absolute;left:0;top:3879px;width:1200px;height:111px;background:var(--footer)}
.footer-links{position:absolute;left:144px;top:30px;font-family:"Lato",sans-serif;font-size:11px;color:var(--footer-text);word-spacing:2px}
.copyright{position:absolute;left:144px;top:62px;font-family:"Lato",sans-serif;font-size:11px;color:var(--footer-text)}
.social{position:absolute;top:43px;width:22px;height:22px;border-radius:50%;background:#8c8c8c}
</style>
</head>
<body>

<header class="hero">
  <svg class="hero-backdrop" width="1200" height="700" viewBox="0 0 1200 700">
    <defs>
      <linearGradient id="heroTone" x1="0" y1="0" x2="1" y2="0.4">
        <stop offset="0" stop-color="#6e8a4a"/>
        <stop offset="0.3" stop-color="#a79c8a"/>
        <stop offset="0.6" stop-color="#5d574f"/>
        <stop offset="1" stop-color="#2b241f"/>
      </linearGradient>
    </defs>
    <rect role="img" aria-label="Family of three walking happily in front of a suburban home" width="1200" height="690" fill="url(#heroTone)"/>
    <rect width="1200" height="90" fill="#000" opacity=".25"/>
    <path d="M0 615 Q600 760 1200 615 L1200 700 L0 700 Z" fill="var(--red)"/>
    <path d="M0 628 Q600 752 1200 628 L1200 700 L0 700 Z" fill="var(--white)"/>
  </svg>
  <div class="brand">Tovira</div>
  <nav class="nav">
    <span class="active" style="left:414px">Home</span>
    <span style="left:505px">About Us</span>
    <span style="left:620px">Services</span>
    <span style="left:726px">News</span>
    <span style="left:810px">Contact us</span>
  </nav>
  <div class="search-ads">Search ads</div>
  <h1 class="hero-title"><span class="line">Vestibulum condimentum</span><span class="line">risus posuere cursus</span></h1>
  <div class="btn" style="left:912px;top:333px;width:144px;height:40px;font-size:20px">Connect</div>
  <svg class="slide-arrow" style="left:45px" viewBox="0 0 42 42"><circle cx="21" cy="21" r="19" fill="none" stroke="#fff" stroke-width="2.5"/><path d="M24 12 L15 21 L24 30" fill="none" stroke="#fff" stroke-width="3"/></svg>
  <svg class="slide-arrow" style="left:1110px" viewBox="0 0 42 42"><circle cx="21" cy="21" r="19" fill="none" stroke="#fff" stroke-width="2.5"/><path d="M18 12 L27 21 L18 30" fill="none" stroke="#fff" stroke-width="3"/></svg>
</header>

<section class="welcome">
  <h2 class="section-title" style="top:772px">Welcome to Tovira</h2>
  <p class="welcome-text">We are an International Non-Profit for Birth Parent Searching.<br>We are a 501(c)(3) non-profit organization that helps Chinese adoptees search and reunite with birth families who were<br>separated due the One Child Policy in China.</p>
  <div class="btn" style="left:536px;top:929px;width:128px;height:41px">Read More</div>
</section>

<section class="steps">
  <div class="steps-bg" role="img" aria-label="Soft pastel background with pink blossoms"></div>
  <h2 class="section-title" style="top:1144px">How we help you connect with your family</h2>
  <div class="step-line" style="left:360px;width:164px"></div>
  <div class="step-line" style="left:677px;width:160px"></div>
  <div class="step-circle" style="left:204px">
    <svg width="80" height="80" viewBox="0 0 80 80" fill="none" stroke="#333" stroke-width="2.5">
      <path d="M14 6 H46 L58 18 V74 H14 Z"/><path d="M46 6 V18 H58"/>
      <path d="M22 28 H48 M22 36 H48 M22 44 H44 M22 52 H38 M22 60 H34"/>
      <path d="M44 66 L66 40 L72 46 L50 72 L42 74 Z"/>
    </svg>
  </div>
  <div class="step-circle" style="left:521px">
    <svg width="84" height="84" viewBox="0 0 84 84" fill="none" stroke="#333" stroke-width="2.5">
      <rect x="8" y="10" width="56" height="44"/>
      <path d="M16 48 V38 M24 48 V32 M32 48 V40"/>
      <path d="M16 26 L30 18 L40 24 L56 14"/>
      <circle cx="56" cy="14" r="3"/>
      <circle cx="54" cy="54" r="12"/><path d="M63 63 L76 76"/>
    </svg>
  </div>
  <div class="step-circle" style="left:837px">
    <svg width="84" height="84" viewBox="0 0 84 84" fill="none" stroke="#333" stroke-width="2.5">
      <circle cx="24" cy="18" r="8"/><circle cx="60" cy="18" r="8"/><circle cx="42" cy="40" r="7"/>
      <path d="M12 70 V40 Q12 30 24 30 Q36 30 36 40 V70"/>
      <path d="M48 70 V40 Q48 30 60 30 Q72 30 72 40 V70"/>
      <path d="M32 76 V58 Q32 50 42 50 Q52 50 52 58 V76"/>
    </svg>
  </div>
  <div class="step" style="left:138px"><div class="step-num">STEP 1</div><div class="step-name">Praesent iaculis</div><p class="step-desc">Maecenas consequat justo enim, ac mattis massa imper-<br>diet quis. Fusce eget neque elit.</p></div>
  <div class="step" style="left:455px"><div class="step-num">STEP 2</div><div class="step-name">Sed augue</div><p class="step-desc">Maecenas consequat justo enim, ac mattis massa imper-<br>diet quis. Fusce eget neque elit.</p></div>
  <div class="step" style="left:771px"><div class="step-num">STEP 3</div><div class="step-name">Proin eget</div><p class="step-desc">Maecenas consequat justo enim, ac mattis massa imper-<br>diet quis. Fusce eget neque elit.</p></div>
</section>

<section class="families">
  <h2 class="section-title" style="top:1666px">Previously Connected Families</h2>
  <article class="card" style="left:144px;top:1730px">
    <div class="card-photo" role="img" aria-label="Family sharing an outdoor dinner" style="background:linear-gradient(160deg,#d8c9a6,#a9785c 55%,#6f4b3b)"></div>
    <h3 class="card-title"><span class="line">Etiam vel massa elementum,</span><span class="line">bibendum tellus venenatis</span></h3>
    <p class="card-text"><span class="line">Quisque aliquet ex nec est vestibulum pulvinar. Pel-</span><span class="line">lentesque convallis molestie enim sit amet efficitur.</span><span class="line">Etiam id imperdiet lectus.</span></p>
    <svg class="card-arrow" width="28" height="24" viewBox="0 0 28 24"><path d="M2 12 H22 M14 3 L23 12 L14 21" fill="none" stroke="var(--arrow)" stroke-width="4"/></svg>
  </article>
  <article class="card" style="left:456px;top:1730px">
    <div class="card-photo" role="img" aria-label="Three generations of a family seated on a sofa" style="background:linear-gradient(160deg,#ece6da,#b9a58a 55%,#6d6256)"></div>
    <h3 class="card-title"><span class="line">Fusce vitae lectus sit amet mi</span><span class="line">pulvinar maximus</span></h3>
    <p class="card-text"><span class="line">Quisque aliquet ex nec est vestibulum pulvinar. Pel-</span><span class="line">lentesque convallis molestie enim sit amet efficitur.</span><span class="line">Etiam id imperdiet lectus.</span></p>
    <svg class="card-arrow" width="28" height="24" viewBox="0 0 28 24"><path d="M2 12 H22 M14 3 L23 12 L14 21" fill="none" stroke="var(--arrow)" stroke-width="4"/></svg>
  </article>
  <article class="card" style="left:768px;top:1730px">
    <div class="card-photo" role="img" aria-label="Family sitting together on the grass in a park" style="background:linear-gradient(160deg,#8fae6a,#c7a78e 55%,#5a6e46)"></div>
    <h3 class="card-title"><span class="line">Aenean placeratvel accumsan</span><span class="line">aliquet, magna nibh accumsan</span></h3>
    <p class="card-text"><span class="line">Quisque aliquet ex nec est vestibulum pulvinar. Pel-</span><span class="line">lentesque convallis molestie enim sit amet efficitur.</span><span class="line">Etiam id imperdiet lectus.</span></p>
    <svg class="card-arrow" width="28" height="24" viewBox="0 0 28 24"><path d="M2 12 H22 M14 3 L23 12 L14 21" fill="none" stroke="var(--arrow)" stroke-width="4"/></svg>
  </article>
  <div class="btn" style="left:536px;top:2142px;width:128px;height:40px">View All</div>
</section>

<section class="story">
  <div class="banner" role="img" aria-label="Soft green blossom background"></div>
  <div class="banner-photo" role="img" aria-label="Mother and adult daughter laughing while looking at a phone"></div>
  <p class="banner-quote"><span class="line">Phasellus nisl est, condimentum</span><span class="line">vitae faucibus in, sollicitudin vel</span><span class="line">metus amet consequat. Integer</span><span class="line">eu massa lacinia, lacinia nulla</span><span class="line">non, volutpat purus.</span></p>
  <div class="btn" style="left:928px;top:2593px;width:127px;height:39px">Read More</div>
</section>

<section class="news">
  <h2 class="section-title" style="top:2823px">News</h2>
  <article class="card" style="left:144px;top:2883px">
    <div class="card-photo" role="img" aria-label="Three generations of a family seated on a sofa" style="background:linear-gradient(160deg,#ece6da,#b9a58a 55%,#6d6256)"></div>
    <h3 class="card-title"><span class="line">Etiam vel massa elementum,</span><span class="line">bibendum tellus venenatis</span></h3>
    <p class="card-text"><span class="line">Quisque aliquet ex nec est vestibulum pulvinar. Pel-</span><span class="line">lentesque convallis molestie enim sit amet efficitur.</span><span class="line">Etiam id imperdiet lectus.</span></p>
    <svg class="card-arrow" width="28" height="24" viewBox="0 0 28 24"><path d="M2 12 H22 M14 3 L23 12 L14 21" fill="none" stroke="var(--arrow)" stroke-width="4"/></svg>
  </article>
  <article class="card" style="left:456px;top:2883px">
    <div class="card-photo" role="img" aria-label="Large government hall lit up at night" style="background:linear-gradient(180deg,#0d1630 0%,#1c2440 45%,#c9b27a 75%,#2a2620 100%)"></div>
    <h3 class="card-title"><span class="line">Fusce vitae lectus sit amet mi</span><span class="line">pulvinar maximus</span></h3>
    <p class="card-text"><span class="line">Quisque aliquet ex nec est vestibulum pulvinar. Pel-</span><span class="line">lentesque convallis molestie enim sit amet efficitur.</span><span class="line">Etiam id imperdiet lectus.</span></p>
    <svg class="card-arrow" width="28" height="24" viewBox="0 0 28 24"><path d="M2 12 H22 M14 3 L23 12 L14 21" fill="none" stroke="var(--arrow)" stroke-width="4"/></svg>
  </article>
  <article class="card" style="left:768px;top:2883px">
    <div class="card-photo" role="img" aria-label="Street with red lanterns hanging from trees" style="background:linear-gradient(160deg,#c23a3a,#8d7a6c 55%,#4b4640)"></div>
    <h3 class="card-title"><span class="line">Aenean placeratvel accumsan</span><span class="line">aliquet, magna nibh accumsan</span></h3>
    <p class="card-text"><span class="line">Quisque aliquet ex nec est vestibulum pulvinar. Pel-</span><span class="line">lentesque convallis molestie enim sit amet efficitur.</span><span class="line">Etiam id imperdiet lectus.</span></p>
    <svg class="card-arrow" width="28" height="24" viewBox="0 0 28 24"><path d="M2 12 H22 M14 3 L23 12 L14 21" fill="none" stroke="var(--arrow)" stroke-width="4"/></svg>
  </article>
  <div class="btn" style="left:536px;top:3296px;width:128px;height:40px">View All</div>
</section>

<section class="contact-section">
  <div class="contact" role="img" aria-label="Red background with faint Chinese paper pattern"></div>
  <h2 class="section-title" style="top:3500px;color:var(--white);font-weight:600">Contact Us</h2>
  <div class="field" style="left:144px;top:3558px;width:217px;height:37px">Name</div>
  <div class="field" style="left:375px;top:3558px;width:217px;height:37px">Family Name</div>
  <div class="field" style="left:606px;top:3558px;width:218px;height:37px">Email</div>
  <div class="field" style="left:838px;top:3558px;width:218px;height:37px">Phone Number</div>
  <div class="field area" style="left:144px;top:3614px;width:912px;height:110px">How can we help</div>
  <div class="btn submit" style="left:536px;top:3753px;width:128px;height:40px">Submit</div>
</section>

<footer class="footer">
  <div class="footer-links">Home &nbsp;|&nbsp; About Us &nbsp;|&nbsp; Services &nbsp;|&nbsp; News &nbsp;|&nbsp; Contact us &nbsp;|&nbsp; Search Ads &nbsp;|&nbsp; Connect</div>
  <div class="copyright">Copyright &copy; 2021 &nbsp; Tovira. &nbsp; All rights reserved.</div>
  <div class="social" style="left:979px"></div>
  <div class="social" style="left:1031px"></div>
</footer>

</body>
</html>
```